Brisas del Valle, I Natural Brisas del Valle

Looking for a logo and packaging design for a retail bag of sugar,

Target Market(s)

Hispanic public

Font styles to use
Serif
Script

Colors
ffffff
add136
fbed22
ec1f27
ffc214
33b8a4

Requirements
Must have
• Central and south America map on the bag
• it must say the quantity (1,8 kg and 4 lb)
Nice to have
• sugar canes pointing at the map, ( Mexico, Central America and South America

```html
<!DOCTYPE html>
<html lang="es">
<head>
<meta charset="utf-8">
<title>Brisas del Valle — Azúcar Natural</title>
<link rel="stylesheet" href="https://fonts.googleapis.com/css2?family=Montserrat:wght@400&family=Russo+One&family=Oswald:wght@500;600&display=swap">
<style>
  :root {
    --canvas: #ececed;
    --bag-light: #f4fcf9;
    --bag-mid: #c3ebe2;
    --bag-edge: #9fd8cb;
    --crimp: #a8ddd0;
    --crimp-line: #8ecdbf;
    --ink: #10382f;
    --cane-light: rgba(255, 255, 255, 0);
    --cane-tone: rgba(120, 190, 174, 0.45);
  }
  * { margin: 0; padding: 0; box-sizing: border-box; }
  html, body { width: 1200px; height: 1200px; overflow: hidden; background: var(--canvas); }
  .canvas { position: relative; width: 1200px; height: 1200px; }

  .bag {
    position: absolute; left: 260px; top: 135px; width: 680px; height: 930px;
    background: radial-gradient(ellipse 55% 45% at 50% 55%, var(--bag-light) 0%, var(--bag-mid) 70%, var(--bag-edge) 100%);
    clip-path: polygon(0 0, 100% 0, 100% 8%, 98.5% 30%, 98.5% 70%, 100% 92%, 100% 100%, 0 100%, 0 92%, 1.5% 70%, 1.5% 30%, 0 8%);
  }
  .crimp {
    position: absolute; left: 0; width: 100%; height: 66px;
    background: repeating-linear-gradient(180deg, var(--crimp) 0 6px, var(--crimp-line) 6px 8px);
  }
  .crimp--top { top: 0; }
  .crimp--bottom { bottom: 0; }

  .cane-field {
    position: absolute; left: 0; top: 66px; width: 100%; height: 798px;
    background:
      radial-gradient(ellipse 38% 34% at 50% 55%, var(--cane-light) 0%, var(--cane-light) 55%, var(--cane-tone) 100%),
      linear-gradient(90deg, var(--cane-tone) 0%, var(--cane-light) 22%, var(--cane-light) 78%, var(--cane-tone) 100%);
  }

  .variety {
    position: absolute; top: 158px; width: 100%; text-align: center;
    font-family: "Montserrat", sans-serif; font-size: 27px; letter-spacing: 1px; color: var(--ink);
  }

  .brand-mark {
    position: absolute; left: 290px; top: 262px; width: 100px; height: 100px; background: var(--ink);
  }
  .brand {
    position: absolute; top: 420px; width: 100%; text-align: center;
    font-family: "Russo One", sans-serif; font-weight: 400; font-size: 80px; line-height: 1;
    text-transform: uppercase; color: var(--ink);
  }
  .descriptor {
    position: absolute; top: 590px; width: 100%; text-align: center;
    font-family: "Oswald", sans-serif; font-weight: 600; font-size: 24px; letter-spacing: 0.3px; color: var(--ink);
  }

  .origin {
    position: absolute; left: 68px; top: 770px; display: flex; gap: 18px; align-items: flex-start;
  }
  .origin-map { width: 42px; height: 68px; border-radius: 45% 50% 40% 30%; background: var(--ink); }
  .origin-text {
    font-family: "Oswald", sans-serif; font-weight: 500; font-size: 19px; line-height: 1.55; color: var(--ink);
  }

  .natural-badge {
    position: absolute; right: 78px; top: 728px; width: 84px; height: 84px;
    border: 2px solid var(--ink); border-radius: 50%;
  }
  .net-weight {
    position: absolute; right: 36px; top: 822px;
    font-family: "Oswald", sans-serif; font-weight: 500; font-size: 21px; color: var(--ink);
  }
</style>
</head>
<body>
<main class="canvas">
  <section class="bag">
    <div class="crimp crimp--top"></div>
    <div class="cane-field" role="img" aria-label="Faint outline sugar cane stalks covering the bag background"></div>

    <p class="variety">AZUCAR NATURAL</p>
    <div class="brand-mark"></div>
    <h1 class="brand">Brisas<br>del Valle</h1>
    <p class="descriptor">FINE GRANULATED PURE REFINES CANE SUGAR</p>

    <div class="origin">
      <div class="origin-map" role="img" aria-label="Map of Mexico, Central and South America"></div>
      <p class="origin-text">PRODUCT OF MEXICO,<br>CENTRAL &amp; SOUTH AMERICA</p>
    </div>

    <div class="natural-badge"></div>
    <p class="net-weight">NET WT : 1.8 KG (4 LB)</p>

    <div class="crimp crimp--bottom"></div>
  </section>
</main>
</body>
</html>
```